We are looking for a simple design that would be uplifting for
upscale drug addicts

MERIDIAN CIRCLE

PLEASE SEE THE LINK FOR TAG LINE AND CONTENT

thank you.

here is all the actual info we need and we want something like this...

http://assets.qlm.brivostore.com/rest/items/7c2910e5b337de81f94a02bd57e644163ab9fe0a6712?uid=bd31c9e2f7a04c18b6e0d44721fa93c5%2fdrafts&expires=1408211537&signature=kTp4WmQxNvLzHa8YbEoRcJsGf2B%3d

The shape and colors don't have to be like what I posted it is only an example.

Target Market(s)

Wall Street, internet and creative types, men, early 30's,
upwardly mobile, drug addicts

current site

bkltornavel.com

now launching new name Meridian Circle

Industry/Entity Type

Drug

Requirements
Must have
• upscale look, great font
Should not have
• a corporate look but should not look like a clinic.

```html
<!DOCTYPE html>
<html lang="en">
<head>
<meta charset="utf-8">
<title>Meridian Circle</title>
<link rel="stylesheet" href="https://fonts.googleapis.com/css2?family=Archivo+Black&family=Arimo:wght@400&display=swap">
<style>
  :root {
    --brand-red: #a80000;
    --deep-red: #9c0000;
    --paper: #ffffff;
    --ink-light: #ffffff;
  }
  html, body {
    margin: 0;
    padding: 0;
    width: 1200px;
    height: 686px;
    overflow: hidden;
    background: var(--paper);
  }
  .card {
    position: relative;
    width: 1200px;
    height: 686px;
    overflow: hidden;
    background: var(--paper);
  }
  .brand-name {
    position: absolute;
    left: 14px;
    top: 38px;
    margin: 0;
    font-family: "Archivo Black", "Arial Black", sans-serif;
    font-weight: 400;
    font-size: 64px;
    letter-spacing: 1px;
    color: var(--brand-red);
    line-height: 1;
  }
  .texture-edge {
    position: absolute;
    left: 0;
    top: 250px;
    width: 1200px;
    height: 140px;
    background: linear-gradient(to bottom, var(--paper) 0%, #e9b3b3 35%, #c44a4a 65%, var(--deep-red) 100%);
  }
  .base-band {
    position: absolute;
    left: 0;
    top: 388px;
    width: 1200px;
    height: 298px;
    background: var(--deep-red);
  }
  .contact {
    position: absolute;
    margin: 0;
    font-family: "Arimo", Arial, sans-serif;
    font-size: 27px;
    line-height: 41px;
    color: var(--ink-light);
    text-align: center;
    white-space: nowrap;
    letter-spacing: 1px;
  }
  .contact--hotline {
    left: 10px;
    width: 610px;
    top: 546px;
  }
  .contact--locations {
    left: 680px;
    width: 520px;
    top: 448px;
    letter-spacing: 0.5px;
  }
  .contact p { margin: 0; }
</style>
</head>
<body>
  <main class="card">
    <h1 class="brand-name">MERIDIAN CIRCLE</h1>

    <div class="texture-edge" role="img" aria-label="Ragged white and red speckled edge where the white top fades into the red band"></div>
    <div class="base-band"></div>

    <section class="contact contact--hotline">
      <p>Phone:&nbsp; (212) 555-0148</p>
      <p>Get Help Now - 24-Hour Hotline</p>
      <p>855-HARBOR-NOW (855-427-2676)</p>
    </section>

    <section class="contact contact--locations">
      <p>Harbor Renewal</p>
      <p>318 West 52nd St. Suite 402</p>
      <p>New York, NY 10028</p>
      <p>Clara Ruth Weller, MD PC</p>
      <p>74 Fulton Row, Suite 1108, New York,</p>
      <p>NY 10038</p>
    </section>
  </main>
</body>
</html>
```